Corvane Alloys Collective Business Card

Design a business card for a new company. Corvane Alloys Collective is a subsidiary of KTP, Inc. (www.ktpreclaims.example)

Target Market(s)

B2B, Manufactures

Industry/Entity Type

Recycling

Contact Information for Business Card

Corvane Alloys Collective, LLC.
48217 North Wendlow Avenue
Alsip IL 60492
P: (312) 555-0143
F: (312) 555-0144
www.corvaneac.example
Email@corvaneac.example

Font styles to use
Sans Serif

Requirements
Must have
• A KTP, Inc. subsidiary company.
Nice to have
• Recycling Solutions. Uncompromised. (slogan)

```html
<!DOCTYPE html>
<html lang="en">
<head>
<meta charset="utf-8">
<title>Corvane Alloys Collective Business Card</title>
<link rel="stylesheet" href="https://fonts.googleapis.com/css2?family=Open+Sans:wght@400;600;700&display=swap">
<style>
  :root {
    --backdrop: #e9e6e1;
    --card-white: #ffffff;
    --navy: #1f2f6e;
    --forest: #2f6b2a;
    --rule: #2f6b2a;
    --lime-light: #bfe34a;
    --lime-dark: #7cbc1e;
    --mark-green: #2e7d32;
    --on-lime: #ffffff;
  }
  * { box-sizing: border-box; margin: 0; padding: 0; }
  html, body { width: 1200px; height: 913px; overflow: hidden; }
  body {
    background: var(--backdrop);
    font-family: "Open Sans", Arial, sans-serif;
    position: relative;
  }
  .card {
    position: absolute;
    top: 306px;
    width: 525px;
    height: 300px;
    border-radius: 18px;
    box-shadow: 0 10px 24px rgba(0,0,0,0.18);
    overflow: hidden;
  }
  .card--front { left: 60px; background: var(--card-white); }
  .card--back {
    left: 615px;
    background: linear-gradient(135deg, var(--lime-light) 0%, var(--lime-dark) 100%);
  }

  .parent-line {
    position: absolute; top: 22px; right: 26px;
    font-size: 11.5px; letter-spacing: 0.6px; color: var(--forest);
    text-transform: uppercase;
  }
  .holder { position: absolute; top: 58px; right: 26px; text-align: right; }
  .holder-name { font-size: 19px; font-weight: 700; color: var(--navy); letter-spacing: 0.5px; }
  .holder-role { font-size: 11px; color: var(--forest); letter-spacing: 0.8px; margin-top: 1px; }
  .holder-rule {
    position: absolute; top: 106px; left: 232px; right: 22px;
    height: 1.5px; background: var(--rule);
  }

  .brand-mark {
    position: absolute; left: 28px; top: 120px;
    display: flex; align-items: center; gap: 10px;
  }
  .brand-dot { width: 22px; height: 22px; border-radius: 50%; background: var(--mark-green); flex: none; }
  .brand-name { font-size: 17px; font-weight: 700; color: var(--mark-green); line-height: 1.15; width: 170px; }

  .address {
    position: absolute; top: 128px; right: 26px; text-align: right;
    font-size: 12.5px; color: var(--navy); line-height: 1.45;
  }

  .contact-rule {
    position: absolute; top: 196px; left: 22px; right: 232px;
    height: 1.5px; background: var(--rule);
  }
  .contacts {
    position: absolute; left: 28px; top: 208px; list-style: none;
    font-size: 13.5px; color: var(--navy); line-height: 20px;
  }
  .contacts li { display: flex; align-items: center; gap: 8px; }
  .contacts svg { width: 12px; height: 12px; flex: none; }

  .back-mark {
    position: absolute; left: 0; right: 0; top: 104px;
    display: flex; align-items: center; justify-content: center; gap: 12px;
  }
  .back-mark .brand-dot { width: 28px; height: 28px; background: var(--mark-green); }
  .back-mark .brand-name { font-size: 24px; width: auto; color: var(--mark-green); }
  .slogan {
    position: absolute; left: 0; right: 0; bottom: 46px; text-align: center;
    font-size: 13px; letter-spacing: 1px; color: var(--on-lime); text-transform: uppercase;
  }
</style>
</head>
<body>

<section class="card card--front" aria-label="Card front">
  <p class="parent-line">A KTP, Inc. subsidiary company</p>
  <div class="holder">
    <p class="holder-name">DARA QUILL</p>
    <p class="holder-role">OWNER</p>
  </div>
  <div class="holder-rule"></div>

  <div class="brand-mark">
    <span class="brand-dot"></span>
    <span class="brand-name">Corvane Alloys Collective</span>
  </div>

  <p class="address">48217 North Wendlow Avenue<br>Alsip IL 60492</p>

  <div class="contact-rule"></div>
  <ul class="contacts">
    <li>
      <svg viewBox="0 0 12 12" aria-hidden="true"><path d="M2.5 1 L4.5 1 L5 3.5 L3.8 4.4 C4.5 6 6 7.5 7.6 8.2 L8.5 7 L11 7.5 L11 9.5 C11 10.4 10.4 11 9.5 11 C5 11 1 7 1 2.5 C1 1.6 1.6 1 2.5 1 Z" fill="#2f6b2a"/></svg>
      (312) 555-0143
    </li>
    <li>
      <svg viewBox="0 0 12 12" aria-hidden="true"><rect x="3" y="1" width="6" height="3.5" fill="#2f6b2a"/><rect x="1" y="5" width="10" height="4.5" rx="1" fill="#2f6b2a"/><rect x="3" y="8" width="6" height="3" fill="#2f6b2a"/></svg>
      (312) 555-0144
    </li>
    <li>
      <svg viewBox="0 0 12 12" aria-hidden="true"><circle cx="6" cy="6" r="5" fill="none" stroke="#2f6b2a" stroke-width="1.3"/><ellipse cx="6" cy="6" rx="2.2" ry="5" fill="none" stroke="#2f6b2a" stroke-width="1"/><line x1="1" y1="6" x2="11" y2="6" stroke="#2f6b2a" stroke-width="1"/></svg>
      www.corvaneac.example
    </li>
    <li>
      <svg viewBox="0 0 12 12" aria-hidden="true"><rect x="1" y="2.5" width="10" height="7" fill="none" stroke="#2f6b2a" stroke-width="1.2"/><path d="M1 2.5 L6 6.5 L11 2.5" fill="none" stroke="#2f6b2a" stroke-width="1.2"/></svg>
      Email@corvaneac.example
    </li>
  </ul>
</section>

<section class="card card--back" aria-label="Card back">
  <div class="back-mark">
    <span class="brand-dot"></span>
    <span class="brand-name">Corvane Alloys Collective</span>
  </div>
  <p class="slogan">Recycling Solutions. Uncompromised</p>
</section>

</body>
</html>
```